BRIM Outreach Partners Business Card Rebrand

Hello Designers! We are looking for help designing our new business card to go in conjunction with our company rebrand. Unfortunately, we have an event mid June that requires we get these printed ASAP (before our new website is launched.) We have a mostly complete Brand Book which I have uploaded to this request for your reference to company information, style, fonts. I've also enclosed our logo file in .eps & .jpg. Attached is a sample business card my boss liked but said was "too simple." I made it in Canva and do not profess to be a designer. NOT FOR DESIGN REFERENCE, ONLY FOR CONTEXT Here is what our old website looks like: https://brimoutreachpartners.com/.

```html
<!DOCTYPE html>
<html lang="en">
<head>
<meta charset="utf-8">
<title>BRIM Outreach Partners – Business Card</title>
<link href="https://fonts.googleapis.com/css2?family=Arimo:wght@400;700&display=swap" rel="stylesheet">
<style>
  :root {
    --stage: #3a3a3a;
    --card: #050505;
    --ink: #ffffff;
    --accent: #4db3e8;
    --muted: #d9d9d9;
    --rule: #6a6a6a;
  }
  * { box-sizing: border-box; margin: 0; padding: 0; }
  html, body { width: 1200px; height: 689px; overflow: hidden; }
  body {
    background: var(--stage);
    font-family: "Arimo", Arial, sans-serif;
    display: flex;
    align-items: center;
    justify-content: center;
    gap: 60px;
  }
  .card {
    width: 525px;
    height: 300px;
    background: var(--card);
    border-radius: 16px;
    position: relative;
    color: var(--ink);
  }
  /* Front */
  .card-front {
    display: flex;
    flex-direction: column;
    align-items: center;
    justify-content: center;
  }
  .brand {
    display: flex;
    align-items: center;
    gap: 16px;
    margin-top: -20px;
  }
  .brand-dot {
    width: 70px;
    height: 70px;
    border-radius: 50%;
    background: var(--accent);
    flex: none;
  }
  .brand-name {
    font-weight: 700;
    font-size: 30px;
    line-height: 1.05;
    color: var(--ink);
    letter-spacing: 0.5px;
  }
  .front-url {
    position: absolute;
    bottom: 44px;
    width: 100%;
    text-align: center;
    font-size: 14px;
    letter-spacing: 0.3px;
    color: var(--ink);
  }
  /* Back */
  .card-back {
    display: flex;
    align-items: center;
    justify-content: center;
    gap: 18px;
  }
  .person { text-align: right; }
  .person-name {
    color: var(--accent);
    font-weight: 700;
    font-size: 24px;
    margin-bottom: 4px;
  }
  .person-role, .person-location {
    font-size: 14px;
    color: var(--muted);
    line-height: 1.3;
  }
  .divider {
    width: 1px;
    height: 70px;
    background: var(--rule);
  }
  .contacts { list-style: none; }
  .contacts li {
    display: flex;
    align-items: center;
    gap: 8px;
    font-size: 14px;
    color: var(--muted);
    line-height: 1.45;
  }
  .contacts svg { width: 12px; height: 12px; flex: none; fill: var(--accent); }
</style>
</head>
<body>
  <section class="card card-front">
    <div class="brand">
      <span class="brand-dot"></span>
      <span class="brand-name">BRIM<br>Outreach Partners</span>
    </div>
    <p class="front-url">www.brimoutreachpartners.com</p>
  </section>

  <section class="card card-back">
    <div class="person">
      <p class="person-name">Daniel Marlow-Grant</p>
      <p class="person-role">Managing Partner</p>
      <p class="person-location">Raleigh, NC based (East)</p>
    </div>
    <span class="divider"></span>
    <ul class="contacts">
      <li>
        <svg viewBox="0 0 24 24" aria-hidden="true"><path d="M6.6 10.8a15.1 15.1 0 0 0 6.6 6.6l2.2-2.2a1 1 0 0 1 1-.25 11.4 11.4 0 0 0 3.6.57 1 1 0 0 1 1 1V20a1 1 0 0 1-1 1A17 17 0 0 1 3 4a1 1 0 0 1 1-1h3.5a1 1 0 0 1 1 1c0 1.25.2 2.45.57 3.57a1 1 0 0 1-.25 1z"/></svg>
        +945-555-0142
      </li>
      <li>
        <svg viewBox="0 0 24 24" aria-hidden="true"><path d="M2 5h20v14H2z M3.5 6.5 12 13l8.5-6.5" fill="var(--accent)" stroke="var(--card)" stroke-width="1.6"/></svg>
        info@brimoutreachpartners.com
      </li>
      <li>
        <svg viewBox="0 0 24 24" aria-hidden="true"><circle cx="12" cy="12" r="10"/><path d="M2 12h20M12 2c3 3 3 17 0 20M12 2c-3 3-3 17 0 20" fill="none" stroke="var(--card)" stroke-width="1.5"/></svg>
        brimoutreachpartners.com
      </li>
    </ul>
  </section>
</body>
</html>
```